Business Card Design

​Silver Harbor Grooves provides personal, friendly service in a fun and high energy environment. We are based in Vermont.

We would like a card that appeals to a wide range of audiences as we do a wide range of events. Please feel free to check out our website silverharborgrooves.com for inspiration.

Target Market(s)

weddings, corporate, birthday parties, colleges

Industry/Entity Type

Business

Contact Information for Business Card

Silver Harbor Grooves
Providing Entertainment For All Occasions
555 218 6093
silverharborgrooves@mailvane.com
silverharborgrooves.com

```html
<!DOCTYPE html>
<html lang="en">
<head>
<meta charset="utf-8">
<title>Silver Harbor Grooves – Business Card</title>
<link rel="stylesheet" href="https://fonts.googleapis.com/css2?family=Lato:wght@400;700;900&display=swap">
<style>
  :root {
    --backdrop: #6e6e6e;
    --card-white: #ffffff;
    --forest: #2f5426;
    --forest-dark: #24431d;
    --swoosh-red: #c8262c;
    --ink: #2b3a27;
    --contact-text: #f1f1ec;
    --tagline-gold: #f2c21b;
  }
  * { margin: 0; padding: 0; box-sizing: border-box; }
  html, body {
    width: 1200px;
    height: 900px;
    overflow: hidden;
    background: var(--backdrop);
  }
  .canvas {
    position: relative;
    width: 1200px;
    height: 900px;
  }
  .business-card {
    position: absolute;
    left: 100px;
    top: 165px;
    width: 1000px;
    height: 570px;
    background: var(--card-white);
    overflow: hidden;
    font-family: "Lato", Arial, sans-serif;
  }
  .card-curves {
    position: absolute;
    inset: 0;
    width: 1000px;
    height: 570px;
  }
  .brand-lockup {
    position: absolute;
    left: 0;
    right: 0;
    top: 70px;
    display: flex;
    flex-direction: column;
    align-items: center;
    gap: 22px;
  }
  .brand-mark {
    width: 96px;
    height: 96px;
    border-radius: 50%;
    background: var(--forest);
  }
  .brand-name {
    font-weight: 900;
    font-size: 54px;
    letter-spacing: 1px;
    text-transform: uppercase;
    color: var(--ink);
    line-height: 1;
  }
  .contact-list {
    position: absolute;
    left: 0;
    right: 0;
    top: 385px;
    text-align: center;
    color: var(--contact-text);
    font-size: 25px;
    line-height: 38px;
    padding-left: 90px;
  }
  .contact-label { font-weight: 700; }
  .tagline {
    position: absolute;
    left: 0;
    right: 0;
    top: 512px;
    text-align: center;
    color: var(--tagline-gold);
    font-size: 27px;
    line-height: 1;
  }
  .tagline-name { font-weight: 900; text-transform: uppercase; }
</style>
</head>
<body>
<main class="canvas">
  <section class="business-card">
    <svg class="card-curves" viewBox="0 0 1000 570" aria-hidden="true">
      <path d="M0,395 Q470,250 1000,350 L1000,570 L0,570 Z" fill="var(--forest)"/>
      <path d="M0,340 Q480,205 1000,325 Q480,228 0,368 Z" fill="var(--swoosh-red)"/>
    </svg>

    <header class="brand-lockup">
      <div class="brand-mark"></div>
      <h1 class="brand-name">Silver Harbor Grooves</h1>
    </header>

    <address class="contact-list" style="font-style: normal;">
      <div><span class="contact-label">phone:</span> 555 218 6093</div>
      <div><span class="contact-label">web:</span> silverharborgrooves.com</div>
      <div><span class="contact-label">email:</span> silverharborgrooves@mailvane.com</div>
    </address>

    <p class="tagline"><span class="tagline-name">Silver Harbor Grooves</span> Providing Entertainment For All Occasions</p>
  </section>
</main>
</body>
</html>
```